Security Company Needs a Website *

We need a website that gives our clients information about the services we provide, methods of contacting us and landing page to advertise on social media sites.

We need five landing pages titled Home, About Us, Services, Contact Us and a Landing Page that can be linked to Chatterlane advertising.

About Us - Should have a section for Core Values & Ethics, Our Vision, Our Mission and Partners.

Services - This page should show the different categories which include CCTV, Security Alarms, Access Control and Fire Protection.

CCTV Service Description:
Closed circuit television (CCTV) has long been implemented by businesses as a surveillance tool in areas that need monitoring. With digital CCTV cameras, multiple video cameras transmit signals through a set of monitors. The cameras provide thorough surveillance of the area.

With vast technological improvements over the last ten years, businesses with CCTV systems can use unique IP cameras and video analytics to monitor traffic flows, people-count, implement facial and number plate recognition. Useful information about customer behaviour and demographics can be discovered too. CCTV helps prevent crime in many industries and can assist with the improvement of industrial processes, safety on transport systems and traffic monitoring.

Security Alarms Service Description:
Alarms systems are electronic devices programmed to alert people to specific dangers and detect intrusions, fire or theft. Security alarms, systems and access control monitoring combine to create an integrated surveillance solution, tailored to your business’ unique requirements. Our surveillance and alarm monitoring services are ideal for perimeter protection from unwanted intruders or potential dangers.

Access Control Services:
An access control system allows for the free flow of authorised personnel while denying entry to unwanted visitors. With walk-in thieves and trespassers shut out, you dramatically reduce your exposure to crime while increasing the security of your employees, visitors, information and assets.

* Control when and who is entering your premises
* Protect employees, assets and information
* Secure an area or sector
* Observe movement
* Integrate with other security systems

Our range of access control systems can be seamlessly linked to other systems in our portfolio. These include Fire Detection Systems, Intruder Alarms, CCTV, and Building Management. A common request involves the need for a CCTV camera to pan around and focus on a door that has been highlighted as a security risk by the access control system.

Fire Protection Service:
To Be Advised

The above copy-writing will also have to be changed.

Contact Us - This form needs to be simple and straightforward to gather the prospects information and we would like to have a call to action on this page. The Contact Us page should also have a wayfindr plot location of our office address.

We would also like to have a link to our chatterlane page on the website.

Target Market(s)

Commercial businesses, building construction developers and property managers.

Industry/Entity Type

Security

Number of Pages Required

5+ page

Font styles to use
Sans Serif

Colors

Designer to choose colors to be used in the design.

Requirements
Must have
• We need to have the same look and feel as well as website features as the following website:
• https://www.kovrangard.com.au/business-security/
• The website must be easy to use and easy to edit as well.

```html
<!DOCTYPE html>
<html lang="en">
<head>
<meta charset="utf-8">
<title>Umbra Security Solutions</title>
<link href="https://fonts.googleapis.com/css2?family=Poppins:wght@300;400;500;600&display=swap" rel="stylesheet">
<style>
:root{
  --cyan:#1ea6df;
  --navy:#1b2558;
  --ink:#4a4a4a;
  --muted:#6b6b6b;
  --line:#e3e3e3;
  --white:#ffffff;
  --sky-top:#1d5fc9;
  --sky-mid:#2f7fe0;
  --sky-low:#7fb2ea;
}
*{box-sizing:border-box;margin:0;padding:0}
html,body{width:1200px;height:1125px;overflow:hidden}
body{font-family:"Poppins",sans-serif;background:var(--white);color:var(--ink);position:relative}
.site-header{position:absolute;left:0;top:0;width:1200px;height:128px;background:var(--white)}
.brand{position:absolute;left:160px;top:44px;display:flex;align-items:center;gap:10px}
.brand-mark{width:34px;height:34px;border-radius:50%;background:var(--navy)}
.brand-name{font-size:17px;font-weight:500;color:var(--navy);line-height:1.1}
.main-nav{position:absolute;left:346px;top:53px;display:flex;gap:34px;font-size:12.5px;font-weight:400;letter-spacing:.3px}
.main-nav a{color:#666;text-decoration:none}
.main-nav a.is-active{color:var(--cyan)}
.main-nav .has-sub::after{content:"";display:inline-block;width:4px;height:4px;border-right:1px solid #888;border-bottom:1px solid #888;transform:rotate(45deg);margin-left:8px;vertical-align:3px}
.header-phone{position:absolute;left:716px;top:53px;display:flex;align-items:center;gap:6px;font-size:12.5px;color:#666;letter-spacing:.4px}
.header-divider{position:absolute;left:854px;top:55px;width:1px;height:14px;background:#ccc}
.header-search{position:absolute;left:868px;top:54px}
.btn{display:inline-flex;align-items:center;justify-content:center;border:3px solid var(--cyan);border-radius:20px;font-weight:500;text-decoration:none}
.btn-secure{position:absolute;left:896px;top:46px;width:142px;height:32px;font-size:10.5px;color:#444}
.hero{position:absolute;left:0;top:128px;width:1200px;height:502px;background:linear-gradient(180deg,var(--sky-top) 0%,var(--sky-mid) 55%,var(--sky-low) 100%)}
.hero-visual{position:absolute;left:640px;top:50px;width:220px;height:452px;background:linear-gradient(180deg,rgba(235,235,235,.35),rgba(220,220,220,.2))}
.hero-kicker{position:absolute;left:161px;top:185px;font-size:11.5px;font-weight:500;color:var(--white)}
.hero-title{position:absolute;left:159px;top:196px;font-size:46px;font-weight:300;color:var(--white);letter-spacing:-.5px}
.hero-sub{position:absolute;left:161px;top:259px;font-size:10.5px;color:var(--white)}
.btn-learn{position:absolute;left:162px;top:300px;width:118px;height:32px;font-size:10.5px;color:var(--white)}
.hero-caption{position:absolute;left:867px;top:88px;border-left:2px solid var(--white);padding-left:8px;height:40px}
.hero-caption strong{display:block;font-size:10.5px;font-weight:500;color:var(--white)}
.hero-caption span{display:block;font-size:10px;color:#27b6ee;line-height:1.35;margin-top:3px}
.slider-arrow{position:absolute;top:236px;width:31px;height:31px;border:1.5px solid var(--white);border-radius:50%}
.slider-arrow svg{position:absolute;left:9px;top:9px}
.prev{left:30px}.next{left:1139px}
.services{position:absolute;left:161px;top:585px;width:878px;height:150px;background:var(--white);display:flex;padding-left:41px}
.service{width:210px;position:relative}
.service h3{font-size:13.5px;font-weight:600;color:#444;line-height:1.12;margin-top:33px}
.service p{font-size:10.5px;color:var(--muted);line-height:1.55;margin-top:16px;width:170px}
.service .rule{position:absolute;left:0;top:124px;width:165px;height:1px;background:var(--line)}
.service .details{position:absolute;left:7px;top:137px;font-size:10.5px;font-weight:500;color:#555}
.service.is-featured .rule{background:var(--cyan)}
.service.is-featured .details{color:var(--cyan);left:0}
.service .icon{position:absolute;right:45px;top:27px}
.section-rule{position:absolute;left:161px;top:795px;width:878px;height:1px;background:var(--line)}
.promo-visual{position:absolute;left:0;top:855px;width:205px;height:94px;background:linear-gradient(90deg,#fff 0%,#e4e4e4 45%,#cfcfcf 100%)}
.promo-text{position:absolute;left:224px;top:860px;font-size:16.5px;font-weight:500;color:#7a7a7a}
.btn-how{position:absolute;left:833px;top:857px;width:142px;height:32px;font-size:10.5px;color:#555}
.about{position:absolute;left:0;top:949px;width:1200px;height:176px;background:var(--navy);text-align:center}
.about-kicker{margin-top:123px;font-size:12px;font-weight:500;color:var(--cyan)}
.about-title{font-size:44px;font-weight:300;color:var(--white);margin-top:1px;line-height:1.2}
</style>
</head>
<body>
<header class="site-header">
  <div class="brand"><span class="brand-mark"></span><span class="brand-name">Umbra Security</span></div>
  <nav class="main-nav">
    <a href="#" class="is-active">HOME</a>
    <a href="#">ABOUT</a>
    <a href="#" class="has-sub">SERVICES</a>
    <a href="#">CONTACT</a>
  </nav>
  <div class="header-phone">
    <svg width="14" height="14" viewBox="0 0 24 24" fill="none" stroke="#1ea6df" stroke-width="2"><path d="M5 3h4l2 5-3 2a12 12 0 0 0 6 6l2-3 5 2v4a2 2 0 0 1-2 2A18 18 0 0 1 3 5a2 2 0 0 1 2-2z"/></svg>
    +44 4000 512396
  </div>
  <span class="header-divider"></span>
  <svg class="header-search" width="14" height="14" viewBox="0 0 24 24" fill="none" stroke="#555" stroke-width="3"><circle cx="10" cy="10" r="6"/><path d="M15 15l6 6"/></svg>
  <a href="#" class="btn btn-secure">Secure your premises</a>
</header>

<section class="hero" role="img" aria-label="Blue sky with a pole carrying several CCTV cameras">
  <div class="hero-visual" role="img" aria-label="CCTV camera pole"></div>
  <p class="hero-kicker">Umbra</p>
  <h1 class="hero-title">Security</h1>
  <p class="hero-sub">Best surveillance tools</p>
  <a href="#" class="btn btn-learn">Learn More</a>
  <div class="hero-caption"><strong>Closed Circuit Television (CCTV)</strong><span>Unique IP cameras and<br>video analytics to monitor</span></div>
  <span class="slider-arrow prev"><svg width="10" height="10" viewBox="0 0 10 10" fill="none" stroke="#fff" stroke-width="1.3"><path d="M6.5 1.5L3 5l3.5 3.5"/></svg></span>
  <span class="slider-arrow next"><svg width="10" height="10" viewBox="0 0 10 10" fill="none" stroke="#fff" stroke-width="1.3"><path d="M3.5 1.5L7 5 3.5 8.5"/></svg></span>
</section>

<section class="services">
  <article class="service">
    <h3>CCTV<br>System</h3>
    <svg class="icon" width="38" height="28" viewBox="0 0 38 28"><path d="M0 3h38v8l-4 5H16v-2H0z" fill="#8a8a8a"/><rect x="14" y="16" width="4" height="10" fill="#8a8a8a"/></svg>
    <p>Implemented by businesses as a surveillance tool.</p>
    <span class="rule"></span><a class="details">Details ›</a>
  </article>
  <article class="service is-featured">
    <h3>Security<br>Alarms</h3>
    <svg class="icon" width="34" height="34" viewBox="0 0 34 34" fill="#1ea6df"><path d="M7 24a10 10 0 0 1 20 0z"/><rect x="3" y="26" width="28" height="4"/><path d="M17 0v5M5 4l3 3M29 4l-3 3" stroke="#1ea6df" stroke-width="2"/><path d="M17 18v6M14 18h6" stroke="#fff" stroke-width="2"/></svg>
    <p>Electronic devices to alert people to specific dangers.</p>
    <span class="rule"></span><a class="details">Details ›</a>
  </article>
  <article class="service">
    <h3>Access<br>Control</h3>
    <svg class="icon" width="26" height="36" viewBox="0 0 26 36"><path d="M6 16V10a7 7 0 0 1 14 0v6" fill="none" stroke="#8a8a8a" stroke-width="3"/><circle cx="13" cy="24" r="12" fill="#8a8a8a"/><circle cx="13" cy="23" r="3" fill="#fff"/><rect x="12" y="24" width="2" height="5" fill="#fff"/></svg>
    <p>Free flow of authorised personnel while denying entry.</p>
    <span class="rule"></span><a class="details">Details ›</a>
  </article>
  <article class="service">
    <h3>Fire<br>Protection</h3>
    <svg class="icon" width="36" height="34" viewBox="0 0 36 34"><path d="M5 8a15 15 0 0 0 26 0" fill="none" stroke="#8a8a8a" stroke-width="2" transform="rotate(180 18 14)"/><circle cx="18" cy="19" r="12" fill="#8a8a8a"/><path d="M18 11c4 4 6 7 3 11a4 4 0 0 1-7-1c0-3 3-4 4-10z" fill="#fff"/></svg>
    <p>Seamlessly linked to include Fire Detection Systems.</p>
    <span class="rule"></span><a class="details">Details ›</a>
  </article>
</section>

<span class="section-rule"></span>

<div class="promo-visual" role="img" aria-label="White CCTV camera"></div>
<p class="promo-text">CCTV systems can use unique IP cameras and video analytics to monitor</p>
<a href="#" class="btn btn-how">How it works</a>

<section class="about">
  <p class="about-kicker">About Umbra Solution</p>
  <h2 class="about-title">Core Values &amp; Ethics</h2>
</section>
</body>
</html>
```